Design Book Cover - Win The Hiring Room

Need assistance designing a compelling cover for an eBook titled "Win The Hiring Room". eBook is a hard hitting, direct tutorial for how to succeed in a job interview. Written by Derek Pollfrey, a senior partner with 20 years interviewing people for employment at one of the largest and most prestigious consulting firms in the world.

Target Market(s)

anyone looking to land a corporate job with Summit 1000 companies

Industry/Entity Type

Consulting

```html
<!DOCTYPE html>
<html lang="en">
<head>
<meta charset="utf-8">
<title>Win The Hiring Room — Book Cover</title>
<link rel="stylesheet" href="https://fonts.googleapis.com/css2?family=Oswald:wght@500;600&family=Roboto+Condensed:wght@700&family=Open+Sans:wght@400&display=swap">
<style>
  :root {
    --stage: #161412;
    --cover-blue: #1f80b5;
    --cover-blue-deep: #186a98;
    --ink-light: #eef3f6;
    --ink-soft: #d4e6f1;
    --rule: rgba(230, 240, 246, 0.65);
    --art-light: #dfe9ef;
    --art-mid: #9fc3d9;
  }
  * { margin: 0; padding: 0; box-sizing: border-box; }
  html, body {
    width: 1200px;
    height: 1031px;
    overflow: hidden;
    background: var(--stage);
  }
  .canvas {
    position: relative;
    width: 1200px;
    height: 1031px;
    display: flex;
    align-items: center;
    justify-content: center;
  }
  .book-cover {
    width: 620px;
    height: 930px;
    background: linear-gradient(180deg, var(--cover-blue) 0%, var(--cover-blue-deep) 100%);
    display: flex;
    flex-direction: column;
    align-items: center;
    padding: 44px 48px 38px;
    text-align: center;
  }
  .book-title {
    font-family: "Oswald", "Arial Narrow", sans-serif;
    font-weight: 600;
    font-size: 96px;
    line-height: 0.98;
    letter-spacing: 1px;
    color: var(--ink-light);
    text-transform: uppercase;
  }
  .title-rule {
    width: 100%;
    margin: 22px 0 14px;
    border-top: 2px dotted var(--rule);
  }
  .book-subtitle {
    font-family: "Oswald", "Arial Narrow", sans-serif;
    font-weight: 500;
    font-size: 19px;
    letter-spacing: 0.5px;
    color: var(--ink-soft);
    text-transform: uppercase;
  }
  .cover-illustration {
    width: 440px;
    height: 400px;
    margin: 30px 0 24px;
    background: linear-gradient(180deg, var(--art-light) 0%, var(--art-mid) 100%);
    opacity: 0.85;
  }
  .author-name {
    font-family: "Roboto Condensed", "Arial Narrow", sans-serif;
    font-weight: 700;
    font-size: 40px;
    letter-spacing: 1px;
    color: var(--ink-light);
    text-transform: uppercase;
  }
  .author-credential {
    margin-top: 10px;
    font-family: "Open Sans", Arial, sans-serif;
    font-size: 14px;
    line-height: 1.4;
    color: var(--ink-soft);
    max-width: 500px;
  }
</style>
</head>
<body>
  <main class="canvas">
    <section class="book-cover">
      <h1 class="book-title">Win The<br>Hiring Room</h1>
      <div class="title-rule"></div>
      <p class="book-subtitle">Direct tutorial for how to succeed in a job interview</p>
      <div class="cover-illustration" role="img" aria-label="Flat pictogram of a candidate and interviewer at a desk, with a row of waiting candidates beside an interview room door"></div>
      <p class="author-name">Derek Pollfrey</p>
      <p class="author-credential">Senior partner with 20 years interviewing people for employment at one of the largest and most prestigious consulting firms in the world.</p>
    </section>
  </main>
</body>
</html>
```